Sale Hang Tag

Design a bright, cheerful, compelling, call to action sale tag for a lighting showroom. The tag will be used to move older or discontinued product at a really good price. Upscale, friendly, neighbor store. Size should be no larger than 4 by 6 inches.

Industry/Entity Type

Call

```html
<!DOCTYPE html>
<html lang="en">
<head>
<meta charset="utf-8">
<title>Sale Hang Tag</title>
<link rel="stylesheet" href="https://fonts.googleapis.com/css2?family=Anton&display=swap">
<style>
  :root {
    --canvas-bg: #ffffff;
    --tag-paper: #ffffff;
    --tag-edge: #d9d9d9;
    --magenta: #e6007e;
    --magenta-bright: #f2109c;
    --crimson: #d4004a;
    --label-white: #ffffff;
  }
  html, body {
    margin: 0;
    padding: 0;
    width: 1200px;
    height: 900px;
    overflow: hidden;
    background: var(--canvas-bg);
  }
  .tag-canvas {
    position: relative;
    width: 1200px;
    height: 900px;
  }
  .hang-tag {
    position: absolute;
    left: 345px;
    top: 12px;
    width: 510px;
    height: 878px;
    box-sizing: border-box;
    background: var(--tag-paper);
    border: 1.5px solid var(--tag-edge);
    border-radius: 40px 40px 255px 255px;
  }
  .clock-icon-area {
    position: absolute;
    left: 555px;
    top: 52px;
    width: 90px;
    height: 106px;
    border-radius: 45px;
    background: var(--magenta);
  }
  .sale-panel {
    position: absolute;
    left: 370px;
    top: 200px;
    width: 460px;
    height: 665px;
    border-radius: 24px 24px 230px 230px;
    background: radial-gradient(ellipse at 60% 68%, var(--magenta-bright) 0%, var(--magenta) 55%, var(--crimson) 100%);
  }
  .sale-word {
    position: absolute;
    left: 600px;
    top: 540px;
    margin: 0;
    transform: translate(-50%, -50%) rotate(-90deg);
    font-family: "Anton", "Oswald", sans-serif;
    font-weight: 400;
    font-size: 200px;
    line-height: 1;
    letter-spacing: 4px;
    color: var(--label-white);
    text-shadow: -3px 2px 3px rgba(122, 0, 64, 0.45);
    white-space: nowrap;
  }
</style>
</head>
<body>
  <main class="tag-canvas">
    <div class="hang-tag"></div>
    <div class="clock-icon-area" role="img" aria-label="Alarm clock icon"></div>
    <div class="sale-panel" role="img" aria-label="Light bulb illustration in magenta"></div>
    <h1 class="sale-word">$ALE</h1>
  </main>
</body>
</html>
```